Business Card Design

We are a Sydney based bespoke Concierge company, providing hospitality services including Concierge staffing, catering, home dining, events, delivery, stallorix, and manage desks in residential apartment services. Our website goes into more detail.

Target Market(s)

corporate clients, upscale residential clients, executives,

Industry/Entity Type

Hospitality

Contact Information for Business Card

David SouthwellDirector of Operations & Customer Experience
Marlowe Concierge
W:www.marloweconcierge-demo.net;
E;peter@marloweconcierge-demo.net
M: 0412 907 281

Font styles to use
Serif

Colors
3176b5
85cae6
d2a4cc
6b449b

Requirements
Must have
• Business name
• Name
• Title
• Tel
• Email
• Website
Nice to have
• Back - facebook , twitter, instagram

```html
<!DOCTYPE html>
<html lang="en">
<head>
<meta charset="utf-8">
<title>Marlowe Concierge — Business Card</title>
<link href="https://fonts.googleapis.com/css2?family=Lato:wght@400;700&display=swap" rel="stylesheet">
<style>
  :root {
    --backdrop: #ebebeb;
    --brand-blue: #1689c2;
    --brand-blue-light: #1ba0d2;
    --brand-blue-deep: #117fba;
    --paper: #ffffff;
    --ink: #1d1d1f;
  }
  * { margin: 0; padding: 0; box-sizing: border-box; }
  html, body {
    width: 1200px; height: 720px; overflow: hidden;
    background: var(--backdrop);
    font-family: "Lato", sans-serif;
  }
  .canvas { position: relative; width: 1200px; height: 720px; }
  .card {
    position: absolute; top: 241px;
    width: 420px; height: 240px;
    border-radius: 13px; overflow: hidden;
  }
  .card--back {
    left: 147px;
    background: linear-gradient(200deg, var(--brand-blue-light) 0%, var(--brand-blue) 55%, var(--brand-blue-deep) 100%);
  }
  .card--front { left: 633px; background: var(--paper); }
  .wordmark {
    position: absolute; left: 25px;
    font-family: "Lato", sans-serif; font-weight: 400;
    font-size: 21px; line-height: 20px; letter-spacing: 0.5px;
    text-transform: uppercase;
  }
  .card--back .wordmark { top: 176px; color: var(--paper); }
  .card--front .wordmark { left: 24px; top: 68px; color: var(--brand-blue); }
  .band {
    position: absolute; left: 0; width: 100%; height: 12px;
    background: linear-gradient(90deg, var(--brand-blue-deep), var(--brand-blue-light) 50%, var(--brand-blue-deep));
  }
  .band--top { top: 0; }
  .band--bottom { bottom: 0; }
  .person { position: absolute; left: 23px; top: 163px; }
  .person__name { color: var(--brand-blue); font-size: 14.5px; font-weight: 400; line-height: 18px; }
  .person__title { color: var(--ink); font-size: 8.6px; line-height: 12px; margin-top: 1px; }
  .divider {
    position: absolute; left: 230px; top: 157px; width: 1.5px; height: 56px;
    background: linear-gradient(180deg, transparent, var(--brand-blue) 20%, var(--brand-blue) 80%, transparent);
  }
  .contacts { position: absolute; left: 241px; top: 163px; list-style: none; }
  .contacts li {
    display: flex; align-items: center; gap: 6px;
    height: 16px; font-size: 9.6px; color: var(--ink);
  }
  .contacts svg { width: 10px; height: 10px; flex: none; }
</style>
</head>
<body>
<main class="canvas">
  <section class="card card--back" aria-label="Card back">
    <div class="wordmark">Marlowe<br>Concierge</div>
  </section>

  <section class="card card--front" aria-label="Card front">
    <div class="band band--top"></div>
    <div class="wordmark">Marlowe<br>Concierge</div>
    <div class="person">
      <p class="person__name">Peter Hollingby</p>
      <p class="person__title">Director of Operations &amp; Customer Experience</p>
    </div>
    <div class="divider"></div>
    <ul class="contacts">
      <li>
        <svg viewBox="0 0 10 10" aria-hidden="true"><rect x="2.5" y="0.5" width="5" height="9" rx="1" fill="none" stroke="#1689c2" stroke-width="1"/><circle cx="5" cy="8" r="0.6" fill="#1689c2"/></svg>
        <span>0412 907 281</span>
      </li>
      <li>
        <svg viewBox="0 0 10 10" aria-hidden="true"><rect x="0.5" y="2" width="9" height="6.5" rx="0.6" fill="#1689c2"/><path d="M0.8 2.4 L5 5.6 L9.2 2.4" fill="none" stroke="#fff" stroke-width="0.9"/></svg>
        <span>peter@marloweconcierge-demo.net</span>
      </li>
      <li>
        <svg viewBox="0 0 10 10" aria-hidden="true"><circle cx="6" cy="4" r="2.8" fill="none" stroke="#1689c2" stroke-width="1.3"/><line x1="4" y1="6" x2="1" y2="9" stroke="#1689c2" stroke-width="1.6" stroke-linecap="round"/></svg>
        <span>www.marloweconcierge-demo.net</span>
      </li>
    </ul>
    <div class="band band--bottom"></div>
  </section>
</main>
</body>
</html>
```